ORVANE Website Design

A professional website is needed for ORVANE, a newly developed entity that helps support the Professional Employer Organization (PEO) industry through web-based systems. These systems are designed to help PEOs comply with regulatory compliance requirements and to facilitate the completion of online state application and renewal forms.

PEOs serve small and medium-sized businesses by handling tasks related to employee payroll, state/federal tax payments, health & WC insurance, and employment law compliance. (Learn more about PEOs from http://www.lumenvark.example/business/peo-services). Because PEOs take on such significant responsibilities for other businesses, many U.S. states require PEO licensing and bonding.

ORVANE was founded to help these PEOs and states increase the efficiency/reliability of this state oversight process through its web-based systems.

Target Market(s)

PEO Industry representatives and state/federal industry regulators

Industry/Entity Type

Industry

Requirements
Must have
• This is a "design-only" job; no coding is needed. Website should be clean and professional with colors that are compatible with the uploaded logo (green/cream). Additional items:

1. The home page design needs to incorporate (a) ORVANE logo (uploaded), (b) descriptive text (below), and (c) images for ORVANE's 3 alliance partners.

2. The site's interior pages (also design only/no coding) should include (a) a header with the ORVANE logo, (b) footer (for items such as a privacy policy, VEROLK logo, etc), (c) vertical menu of links specific to each service

Primary text for home page:

PEO regulatory compliance made easier … better!
➢ Increase efficiency and reliability of registration/licensing
➢ Reduce errors, omissions and late filings
➢ Save time and money

The ORVANE Alliance
➢ PEO Industry Partners
➢ PEOs
➢ State Regulatory Agencies

Join the Team!

```html
<!DOCTYPE html>
<html lang="en">
<head>
<meta charset="utf-8">
<title>ORVANE – PEO regulatory compliance</title>
<link href="https://fonts.googleapis.com/css2?family=Ubuntu:wght@400;500;700&display=swap" rel="stylesheet">
<style>
:root{
  --green:#4cae3c;
  --green-dark:#2f8a22;
  --ink:#222;
  --muted:#8a8a8a;
  --rule:#dcdcdc;
  --band:#f4f4f4;
  --footer:#2b2b2b;
  --footer-bar:#3a3a3a;
  --footer-text:#9a9a9a;
}
*{box-sizing:border-box;margin:0;padding:0}
html,body{width:784px;height:1200px;overflow:hidden}
body{font-family:"Ubuntu",sans-serif;color:var(--ink);background:#fff;position:relative}
a{color:inherit;text-decoration:none}

.site-header{position:absolute;top:0;left:0;width:784px;height:41px;background:linear-gradient(#fdfdfd,#ececec);box-shadow:0 1px 3px rgba(0,0,0,.25);z-index:2}
.brand{position:absolute;left:85px;top:8px;font-size:22px;font-weight:700;color:var(--green-dark);letter-spacing:1px;display:flex;align-items:center;gap:6px}
.brand i{display:block;width:12px;height:12px;background:var(--green)}
.main-nav{position:absolute;left:388px;top:0;display:flex;height:41px}
.main-nav a{display:flex;align-items:center;padding:0 13px;font-size:9.5px;color:#888;border-right:1px solid #ddd}
.main-nav a.active{background:var(--green);color:#fff;font-weight:500;width:61px;justify-content:center;align-items:flex-start;padding-top:14px;font-size:10px}

.hero{position:absolute;top:41px;left:0;width:784px;height:299px;background:linear-gradient(100deg,#8b9bb8 0%,#c7c9cf 30%,#b25a2a 55%,#7a3a18 70%,#b64a3e 85%,#3c3626 100%)}
.slider-dots{position:absolute;top:348px;left:372px;display:flex;gap:7px}
.slider-dots span{width:8px;height:8px;border-radius:50%;background:#aaa;box-shadow:inset 0 1px 2px rgba(0,0,0,.4)}
.slider-dots span.on{background:#fff;border:2px solid #888}

.intro{position:absolute;left:85px;top:383px;width:405px}
h2{font-weight:400;font-size:14px;color:var(--ink)}
h2 em{font-style:normal;color:var(--green)}
.lead{margin-top:7px;font-size:7.4px;line-height:11.7px;color:var(--muted);padding-bottom:10px;border-bottom:1px solid var(--rule)}
.benefit{display:flex;padding:13px 0 13px 0;border-bottom:1px solid var(--rule)}
.benefit:last-child{border-bottom:0}
.benefit svg{width:40px;height:48px;flex:none;margin-right:12px}
.benefit h3{font-weight:400;font-size:10px;margin-top:2px}
.benefit p{font-size:7.2px;line-height:11.7px;color:var(--muted);margin-top:3px}
.btn{display:inline-block;margin-top:6px;background:linear-gradient(#d7f5cc,#9de08a);border:1px solid var(--green);color:#235a1a;font-size:7px;padding:2px 8px}

.news{position:absolute;left:502px;top:383px;width:196px}
.news-item{padding:8px 0;border-bottom:1px solid var(--rule)}
.news-item:last-child{border-bottom:0}
.news-item h4{font-weight:400;font-size:9.6px}
.news-item time{display:block;font-size:7px;font-style:italic;color:var(--green);margin-top:2px}
.news-item p{font-size:7.2px;line-height:11.7px;color:var(--muted);margin-top:2px;padding-right:10px}

.alliance{position:absolute;left:0;top:708px;width:784px;height:184px;background:linear-gradient(var(--band),#fff 40%,#fff 80%,var(--band));border-top:1px solid #eee}
.alliance h2{position:absolute;left:85px;top:38px}
.alliance-grid{position:absolute;left:85px;top:70px;display:flex}
.partner{display:flex;width:209px}
.partner svg{width:40px;height:44px;flex:none;margin-right:12px;margin-top:4px}
.partner h3{font-weight:400;font-size:10px}
.partner p{font-size:7px;line-height:11.7px;color:var(--muted);margin-top:5px;width:146px}

.partner-logos{position:absolute;left:85px;top:941px;width:614px;display:flex;justify-content:space-between;align-items:center}
.partner-logos span{width:48px;height:22px;background:#c9c9c9;border-radius:3px}

.site-footer{position:absolute;left:0;top:1016px;width:784px;height:154px;background:var(--footer);color:var(--footer-text);font-size:8px}
.footer-col{position:absolute;top:22px;width:145px}
.footer-col h5{color:#fff;font-weight:500;font-size:10px;padding-bottom:6px;border-bottom:1px solid #444;margin-bottom:6px}
.links{display:grid;grid-template-columns:66px 1fr;line-height:10px;color:#ddd}
.tweet{line-height:10.5px;margin-bottom:8px}
.tweet a{color:#ddd}
.contact-line{display:flex;gap:5px;line-height:10px;margin-bottom:6px}
.contact-line svg{width:10px;height:10px;flex:none;fill:#fff}
.contact-line b{color:#fff;font-weight:500}
.subscribe{display:flex;margin-top:6px}
.subscribe span{flex:1;background:#222;border:1px solid #3d3d3d;font-style:italic;font-size:7px;padding:5px 6px;color:#888}
.subscribe b{background:#333;color:#fff;font-weight:400;font-size:7px;padding:5px 8px}
.social{display:flex;gap:3px;margin-top:6px}
.social i{width:14px;height:14px;background:#4a8fd0;border-radius:2px}
.social i:nth-child(5){background:#c83a2e}
.social i:nth-child(6){background:#e8742a}
.footer-bar{position:absolute;left:0;top:1170px;width:784px;height:30px;background:var(--footer-bar);color:var(--footer-text);font-size:7px;text-align:center;line-height:30px}
</style>
</head>
<body>

<header class="site-header">
  <a class="brand" href="#"><i></i>ORVANE</a>
  <nav class="main-nav">
    <a class="active" href="#">Home</a>
    <a href="#">About Us</a>
    <a href="#">Services</a>
    <a href="#">FAQs</a>
    <a href="#">Contact Us</a>
  </nav>
</header>

<div class="hero" role="img" aria-label="Photo of a wooden judge's gavel in front of a flag and a law book"></div>
<div class="slider-dots"><span></span><span class="on"></span><span></span></div>

<section class="intro">
  <h2>PEO regulatory compliance made easier... <em>Better!</em></h2>
  <p class="lead">This is the editor's version of Lorem Ipsum. Proin gravida nibh vel velit auctor aliquet. Aenean sollicitudin, lorem quis bibendum auctor, nisi elit consequat ipsum, nec sagittis sem nibh id elit. Duis sed odio sit amet nibh vulputate cursus a sit amet mauris. Morbi accumsan ipsum velit. Nam nec tellus a odio tincidunt auctor a ornare odio. Sed non mauris vitae erat.</p>

  <article class="benefit">
    <svg viewBox="0 0 40 48"><path d="M20 2 L37 20 H27 V44 H13 V20 H3 Z" fill="#3a7fd0" stroke="#1d4f8f" stroke-width="1.5"/></svg>
    <div><h3>Increase efficiency and reliability of registration and licensing</h3>
    <p>Mauris in erat justo. Nullam ac urna eu felis dapibus condimentum sit amet a augue. Sed non neque elit. Sed ut imperdiet nisi. Proin condimentum.</p>
    <a class="btn" href="#">read more</a></div>
  </article>
  <article class="benefit">
    <svg viewBox="0 0 40 48"><circle cx="20" cy="24" r="17" fill="#f6d8c8" stroke="#e2572a" stroke-width="4"/><line x1="8" y1="12" x2="32" y2="36" stroke="#e2572a" stroke-width="4"/></svg>
    <div><h3>Reduce errors, omissions and late filings</h3>
    <p>This is the editor's version of Lorem Ipsum. Proin gravida nibh vel velit auctor aliquet. Aenean sollicitudin, lorem quis bibendum auctor.</p>
    <a class="btn" href="#">read more</a></div>
  </article>
  <article class="benefit">
    <svg viewBox="0 0 40 48"><circle cx="20" cy="24" r="17" fill="#fff" stroke="#3a6fa8" stroke-width="3"/><path d="M20 24 L20 12 M20 24 L29 27" stroke="#222" stroke-width="2" fill="none"/><path d="M5 18 A16 16 0 0 1 14 8" stroke="#4cae3c" stroke-width="3" fill="none"/></svg>
    <div><h3>Save time and money</h3>
    <p>Sagittis sem nibh id elit. Duis sed odio sit amet nibh vulputate cursus a sit amet mauris. Morbi accumsan ipsum velit. Nam nec tellus a odio tincidunt auctor a ornare odio.</p>
    <a class="btn" href="#">read more</a></div>
  </article>
</section>

<aside class="news">
  <h2>Latest News</h2>
  <div class="news-item"><h4>Proin gravida nibh vel velit auctor aliquet</h4><time>Dec 22, 2012</time><p>Sagittis sem nibh id elit. Duis sed odio sit amet nibh vulputate cursus a sit amet mauris. Morbi accumsan ipsum velit.</p></div>
  <div class="news-item"><h4>Gravida nibh vel velit auctor aliquet</h4><time>Dec 22, 2012</time><p>Sagittis sem nibh id elit. Duis sed odio sit amet nibh vulputate cursus a sit amet mauris. Morbi accumsan ipsum velit.</p></div>
  <div class="news-item"><h4>Proin gravida nibh vel velit auctor aliquet</h4><time>Dec 22, 2012</time><p>Sagittis sem nibh id elit. Duis sed odio sit amet nibh vulputate cursus a sit amet mauris. Morbi accumsan ipsum velit.</p></div>
  <div class="news-item"><h4>Lorem avida nibh vel velit auctor aliquet</h4><time>Dec 22, 2012</time><p>Sagittis sem nibh id elit. Duis sed odio sit amet nibh vulputate cursus a sit amet mauris. Morbi accumsan ipsum velit.</p></div>
</aside>

<section class="alliance">
  <h2>The ORVANE Alliance</h2>
  <div class="alliance-grid">
    <div class="partner">
      <svg viewBox="0 0 40 44"><circle cx="20" cy="22" r="19" fill="#3d8fd8"/><path d="M8 16 q6 -6 12 0 q2 8 -6 10 z M24 26 q8 -2 10 6 q-6 6 -10 0 z" fill="#7fc46a"/></svg>
      <div><h3>PEO Industry Partners</h3><p>Mauris in erat justo. Nullam ac urna eu felis dapibus condimentum sit amet a augue. Sed non neque elit.</p><a class="btn" href="#">Join the team</a></div>
    </div>
    <div class="partner">
      <svg viewBox="0 0 40 44"><path d="M20 2 L37 8 V22 C37 32 28 39 20 42 C12 39 3 32 3 22 V8 Z" fill="#9dcf3a" stroke="#8a8a8a" stroke-width="2"/></svg>
      <div><h3>PEOs</h3><p>Mauris in erat justo. Nullam ac urna eu felis dapibus condimentum sit amet a augue. Sed non neque elit.</p><a class="btn" href="#">Join the team</a></div>
    </div>
    <div class="partner">
      <svg viewBox="0 0 40 44"><circle cx="20" cy="12" r="9" fill="#e8b88a"/><path d="M4 44 V32 C4 25 10 22 20 22 C30 22 36 25 36 32 V44 Z" fill="#6e8aa6"/></svg>
      <div><h3>State Regulatory Agencies</h3><p>Mauris in erat justo. Nullam ac urna eu felis dapibus condimentum sit amet a augue. Sed non neque elit.</p></div>
    </div>
  </div>
</section>

<div class="partner-logos" aria-label="Partner badges">
  <span></span><span></span><span></span><span></span><span></span><span></span><span></span><span></span><span></span><span></span>
</div>

<footer class="site-footer">
  <div class="footer-col" style="left:85px">
    <h5>Quick Links</h5>
    <div class="links">
      <div>Home<br>About Us<br>Contact Us<br>Terms<br>Products<br>Downloads<br>Aenean<br>Sollicitudin</div>
      <div>Lorem Ipsum<br>Proin<br>Gravida<br>Nibh vel velit<br>Auctor aliquet</div>
    </div>
  </div>
  <div class="footer-col" style="left:242px">
    <h5>Latest Tweets</h5>
    <p class="tweet">Proin gravida nibh vel velit auctor aliquet. Aenean sollicitudin, lorem <a href="#">http://orvane.example/news</a></p>
    <p class="tweet">Proin gravida nibh vel velit auctor aliquet. Aenean sollicitudin, lorem <a href="#">http://orvane.example/news</a></p>
  </div>
  <div class="footer-col" style="left:398px">
    <h5>Contact Details</h5>
    <div class="contact-line"><svg viewBox="0 0 10 10"><path d="M5 0 A3.5 3.5 0 0 1 8.5 3.5 C8.5 6 5 10 5 10 C5 10 1.5 6 1.5 3.5 A3.5 3.5 0 0 1 5 0 Z M5 2 A1.5 1.5 0 1 0 5 5 A1.5 1.5 0 1 0 5 2Z"/></svg><div><b>Address:</b> Troin gravida nibh vel,<br>&nbsp;&nbsp;&nbsp;&nbsp;&nbsp;&nbsp;&nbsp;&nbsp;&nbsp;&nbsp;30 Aelit auctor<br>&nbsp;&nbsp;&nbsp;&nbsp;&nbsp;&nbsp;&nbsp;&nbsp;&nbsp;&nbsp;Canada</div></div>
    <div class="contact-line"><svg viewBox="0 0 10 10"><path d="M2 0 L4 2.5 L3 4 C4 6 5 7 6 7 L7.5 6 L10 8 L8 10 C4 10 0 6 0 2 Z"/></svg><div><b>Phone:</b> +10 555 014-220</div></div>
    <div class="contact-line"><svg viewBox="0 0 10 10"><rect x="2" y="0" width="6" height="3"/><rect x="0" y="3.5" width="10" height="4"/><rect x="2" y="8" width="6" height="2"/></svg><div><b>Fax:</b> +10 555 014-221</div></div>
    <div class="contact-line"><svg viewBox="0 0 10 10"><rect x="0" y="0" width="10" height="10" rx="1"/></svg><div><b>Email:</b> <a href="#" style="color:#ddd">contact@orvane.example</a></div></div>
  </div>
  <div class="footer-col" style="left:555px">
    <h5>Subscribe Newsletter</h5>
    <p style="line-height:10.5px">Proin gravida nibh vel velit auctor aliquet. Aenean sollicitudin, lorem</p>
    <div class="subscribe"><span>email address</span><b>Go</b></div>
    <h5 style="margin-top:10px">Follow Us</h5>
    <div class="social"><i></i><i></i><i></i><i></i><i></i><i></i></div>
  </div>
</footer>
<div class="footer-bar">© Copyright 2013 &nbsp;|&nbsp; All Rights Reserved &nbsp;|&nbsp; Privacy Policy</div>

</body>
</html>
```